Ostrel Appraisals BV business cards (a financial services company)

I am looking for a business card design that stands out in the financial advisory field of business & intellectual property valuation. The business card design should be conservative, yet different. Address details have changed since the attached business card. New address is:

Molenvlietkade 27
4817 KT Leiden
The Netherlands

Telephone number remains the same.

```html
<!DOCTYPE html>
<html lang="en">
<head>
<meta charset="utf-8">
<title>Ostrel Appraisals BV – Business Cards</title>
<link rel="stylesheet" href="https://fonts.googleapis.com/css2?family=Nunito+Sans:wght@300;400;600&display=swap">
<style>
  :root {
    --canvas: #e6e6e6;
    --card-white: #ffffff;
    --panel-dark: #474747;
    --panel-mid: #7b7b7b;
    --logo-grey: #7d7d7d;
    --text-light: #ffffff;
    --text-soft: #f0f0f0;
    --shadow: rgba(0,0,0,0.18);
  }
  * { box-sizing: border-box; margin: 0; padding: 0; }
  html, body {
    width: 1200px; height: 800px; overflow: hidden;
    background: var(--canvas);
    font-family: "Nunito Sans", Arial, sans-serif;
  }
  .canvas { position: relative; width: 1200px; height: 800px; }

  .card {
    position: absolute;
    width: 560px; height: 320px;
    background: var(--card-white);
    box-shadow: 0 10px 30px var(--shadow);
    overflow: hidden;
  }
  .card--front { left: 80px; top: 70px; }
  .card--back  { left: 560px; top: 410px; }

  /* Wordmark */
  .wordmark {
    display: flex; align-items: center; gap: 12px;
    color: var(--logo-grey);
    font-weight: 300;
    text-transform: uppercase;
    letter-spacing: 0.06em;
    white-space: nowrap;
  }
  .wordmark__square {
    width: 14px; height: 14px;
    background: var(--logo-grey);
    flex: none;
  }
  .card--front .wordmark {
    position: absolute; left: 50%; top: 50%;
    transform: translate(-50%, -50%);
    font-size: 30px;
  }

  /* Back side */
  .back__white {
    position: absolute; right: 0; top: 0;
    width: 52%; height: 48%;
    display: flex; align-items: center; justify-content: center;
  }
  .back__white .wordmark { font-size: 19px; gap: 9px; }
  .back__white .wordmark__square { width: 10px; height: 10px; }

  .back__mid {
    position: absolute; left: 0; bottom: 0;
    width: 100%; height: 52%;
    background: var(--panel-mid);
  }
  .back__mid--right {
    position: absolute; right: 0; top: 48%;
    width: 52%; height: 12%;
    background: var(--panel-mid);
  }
  .back__dark {
    position: absolute; left: 0; top: 0;
    width: 48%; height: 58%;
    background: var(--panel-dark);
    padding: 58px 0 0 30px;
    color: var(--text-light);
  }
  .back__divider {
    position: absolute; left: 0; top: 58%;
    width: 48%; height: 4px;
    background: var(--card-white);
  }

  .person__name {
    font-size: 18px; font-weight: 400;
    letter-spacing: 0.04em; text-transform: uppercase;
  }
  .person__creds { font-size: 10px; letter-spacing: 0.04em; }
  .person__role { font-size: 14px; font-weight: 300; margin-top: 1px; }
  .services {
    margin-top: 26px;
    font-size: 12.5px; font-weight: 300;
    letter-spacing: 0.05em; text-transform: uppercase; line-height: 1.25;
  }

  .address {
    position: absolute; right: 26px; top: 54%;
    text-align: right;
    color: var(--text-soft);
    font-size: 12.5px; font-weight: 300; line-height: 1.35;
  }

  .contacts {
    position: absolute; left: 30px; bottom: 22px;
    list-style: none;
    color: var(--text-light);
    font-size: 13.5px; font-weight: 300;
  }
  .contacts li { display: flex; align-items: center; gap: 10px; line-height: 1.5; }
  .contacts svg {
    width: 15px; height: 15px; flex: none;
  }
</style>
</head>
<body>
<main class="canvas">

  <section class="card card--front" aria-label="Card front">
    <div class="wordmark"><span class="wordmark__square"></span>Ostrel Appraisals</div>
  </section>

  <section class="card card--back" aria-label="Card back">
    <div class="back__white">
      <div class="wordmark"><span class="wordmark__square"></span>Ostrel Appraisals</div>
    </div>
    <div class="back__mid"></div>
    <div class="back__mid--right"></div>

    <div class="back__dark">
      <p class="person__name">Martin Vale, <span class="person__creds">CFA, ASA, RV</span></p>
      <p class="person__role">Managing Director</p>
      <p class="services">Business and Intellectual<br>Property Valuations</p>
    </div>
    <div class="back__divider"></div>

    <address class="address" style="font-style:normal">
      Molenvlietkade 27<br>4817 KT Leiden<br>The Netherlands
    </address>

    <ul class="contacts">
      <li>
        <svg viewBox="0 0 16 16" aria-hidden="true"><rect width="16" height="16" rx="2" fill="#3c3c3c"/><path d="M5 4l2 2-1 1.2c.6 1.3 1.5 2.2 2.8 2.8L10 9l2 2-1.3 1.3C7.5 12 4 8.5 3.7 5.3z" fill="#fff"/></svg>
        +31 (0)70 384 1926
      </li>
      <li>
        <svg viewBox="0 0 16 16" aria-hidden="true"><rect width="16" height="16" rx="2" fill="#3c3c3c"/><rect x="3.5" y="5" width="9" height="6.5" fill="none" stroke="#fff" stroke-width="1"/><path d="M3.5 5l4.5 3.5L12.5 5" fill="none" stroke="#fff" stroke-width="1"/></svg>
        mvale@ostrelappraisals.com
      </li>
      <li>
        <svg viewBox="0 0 16 16" aria-hidden="true"><rect width="16" height="16" rx="2" fill="#3c3c3c"/><circle cx="8" cy="8" r="4.5" fill="none" stroke="#fff" stroke-width="1"/><ellipse cx="8" cy="8" rx="2" ry="4.5" fill="none" stroke="#fff" stroke-width="0.8"/><path d="M3.5 8h9" stroke="#fff" stroke-width="0.8"/></svg>
        www.ostrelappraisals.com
      </li>
    </ul>
  </section>

</main>
</body>
</html>
```